Corporate Business Card

Very professional, Modern, Not to busy, include phone address email, website
(253) 555-0174, 61807 19th Street N, Kent, WA 98517, marcus@kestrelbayholding.com, brelvanindustries.com

Target Market(s)

Manufacturing

Industry/Entity Type

Aero, machining, manufacturing, Off road racing

Contact Information for Business Card

Phone, address email, website

```html
<!DOCTYPE html>
<html lang="en">
<head>
<meta charset="utf-8">
<title>Brelvan Industries – Business Card</title>
<link rel="stylesheet" href="https://fonts.googleapis.com/css2?family=PT+Sans:wght@400;700&display=swap">
<style>
  :root {
    --navy: #173673;
    --navy-deep: #122d63;
    --navy-soft: #1c3c7a;
    --red: #d9252a;
    --grey-text: #58595b;
    --grey-stripe: #8c8d8f;
    --paper: #ffffff;
    --backdrop: #98999a;
  }
  * { box-sizing: border-box; margin: 0; padding: 0; }
  html, body {
    width: 1200px; height: 1200px; overflow: hidden;
    background: var(--backdrop);
    font-family: "PT Sans", sans-serif;
  }
  .card {
    position: absolute; left: 231px; width: 736px; height: 451px; overflow: hidden;
  }
  .card--front { top: 116px; background: var(--paper); }
  .card--back {
    top: 631px;
    background: linear-gradient(180deg, var(--navy-soft) 0%, var(--navy-deep) 100%);
  }
  .brand {
    position: absolute; left: 45px; top: 62px;
    font-weight: 700; font-size: 46px; line-height: 1; color: var(--navy);
    letter-spacing: 0.5px;
  }
  .holder {
    position: absolute; right: 45px; top: 196px; text-align: right;
  }
  .holder__name { font-size: 36px; color: var(--navy); line-height: 1.1; }
  .holder__title { font-size: 23px; color: var(--red); line-height: 1.2; }
  .divider {
    position: absolute; left: 45px; right: 45px; top: 277px;
    height: 2px; background: var(--red);
  }
  .contacts {
    position: absolute; left: 45px; top: 308px; list-style: none;
  }
  .contacts li {
    display: flex; align-items: center; height: 30px;
    font-size: 19px; color: var(--grey-text);
  }
  .contacts svg { width: 20px; height: 20px; margin-right: 14px; flex: none; }
  .address {
    position: absolute; right: 45px; top: 308px; text-align: right;
    font-size: 19px; line-height: 27px; color: var(--grey-text);
  }
  .address svg { width: 16px; height: 20px; vertical-align: -3px; margin-right: 14px; }
  .swoosh { position: absolute; left: 0; top: 0; width: 736px; height: 451px; }
  .brand--reverse {
    position: absolute; left: 0; right: 0; top: 190px; text-align: center;
    font-weight: 700; font-size: 60px; line-height: 1; color: var(--paper);
    letter-spacing: 0.5px;
  }
</style>
</head>
<body>
  <section class="card card--front">
    <div class="brand">Brelvan Industries</div>

    <div class="holder">
      <div class="holder__name">Dorian Walsh</div>
      <div class="holder__title">President</div>
    </div>

    <div class="divider"></div>

    <ul class="contacts">
      <li>
        <svg viewBox="0 0 24 24" aria-hidden="true"><path fill="var(--navy)" d="M6.6 10.8c1.4 2.8 3.8 5.1 6.6 6.6l2.2-2.2c.3-.3.7-.4 1-.2 1.1.4 2.3.6 3.6.6.6 0 1 .4 1 1V20c0 .6-.4 1-1 1C10.6 21 3 13.4 3 4c0-.6.4-1 1-1h3.5c.6 0 1 .4 1 1 0 1.3.2 2.5.6 3.6.1.3 0 .7-.2 1z"/></svg>
        (253) 555-0174
      </li>
      <li>
        <svg viewBox="0 0 24 24" aria-hidden="true"><rect x="1" y="4" width="19" height="13" rx="1" fill="var(--navy)"/><path d="M2 5l8.5 6.5L19 5" stroke="#fff" stroke-width="1.6" fill="none"/><circle cx="19" cy="18" r="4.5" fill="var(--navy)" stroke="#fff" stroke-width="1"/><path d="M16.8 18l1.6 1.6 2.8-3" stroke="#fff" stroke-width="1.4" fill="none"/></svg>
        marcus@kestrelbayholding.com
      </li>
      <li>
        <svg viewBox="0 0 24 24" aria-hidden="true"><g fill="none" stroke="var(--navy)" stroke-width="1.6"><circle cx="12" cy="12" r="10"/><ellipse cx="12" cy="12" rx="4.5" ry="10"/><path d="M2 12h20M4 6.5h16M4 17.5h16"/></g></svg>
        brelvanindustries.com
      </li>
    </ul>

    <div class="address">
      <div><svg viewBox="0 0 16 20" aria-hidden="true"><path fill="var(--navy)" d="M8 0C3.6 0 0 3.5 0 7.8 0 13.5 8 20 8 20s8-6.5 8-12.2C16 3.5 12.4 0 8 0zm0 11a3.2 3.2 0 1 1 0-6.4A3.2 3.2 0 0 1 8 11z"/></svg>61807 19th</div>
      <div>Street N, Kent, WA 98517</div>
    </div>

    <svg class="swoosh" viewBox="0 0 920 564" preserveAspectRatio="none" aria-hidden="true">
      <path fill="var(--grey-stripe)" d="M0,505 C70,526 210,531 400,519 L400,523 C210,540 70,537 0,522 Z"/>
      <path fill="var(--red)" d="M380,521 C520,497 630,480 700,481 C800,483 870,497 920,506 L920,535 C860,512 790,502 700,504 C620,506 500,518 380,524 Z"/>
      <path fill="var(--navy)" d="M0,533 C200,546 450,522 640,504 C760,494 850,505 920,541 L920,564 L0,564 Z"/>
    </svg>
  </section>

  <section class="card card--back">
    <div class="brand--reverse">Brelvan Industries</div>
  </section>
</body>
</html>
```